Torvel & Company: Business Cards, Stationery & Envelopes
Our Tagline is "Be Heard."
Simple
Marla Drosset
Founder, Torvel & Company
217 Meadow Lantern Dr.
Fernwood, Ohio 27584
2816 Halloway Brook, NE
Ashford, Kansas 30361
Marla@TorvelAndCo.example
www.TorvelAndCo.example
My consulting firm helps CEOs and other high-level executives with high-stakes communications. Our materials must exude professionalism and a modern, fresh, crisp and clean feel. The business cards, stationery and envelopes should match the look and feel of the logo and website. I'm interested in seeing designs that incorporate our "Be Heard" tagline, as well as ones that don't.
I think I prefer a card that is single-sided, but if you think there's a cool design that puts some information such as our addresses on back, I'm open to it.
Here are the relevant logo files

```html
<!DOCTYPE html>
<html lang="en">
<head>
<meta charset="utf-8">
<title>Torvel &amp; Company — Business Cards</title>
<link href="https://fonts.googleapis.com/css2?family=Cinzel:wght@600&family=Arimo:wght@400;700&display=swap" rel="stylesheet">
<style>
  :root {
    --page: #ece9e4;
    --card-white: #ffffff;
    --ink: #3a3a3a;
    --red: #d0111b;
    --red-deep: #8f0a10;
    --maroon: #3e0607;
    --wave-gray: #9a9a9a;
    --text-light: #ffffff;
  }
  * { margin: 0; padding: 0; box-sizing: border-box; }
  html, body { width: 1200px; height: 911px; overflow: hidden; background: var(--page); }
  .canvas { position: relative; width: 1200px; height: 911px; }

  .card {
    position: absolute; width: 420px; height: 234px;
    border-radius: 10px; overflow: hidden;
    box-shadow: 0 6px 18px rgba(0,0,0,.28);
    font-family: "Arimo", Arial, sans-serif;
  }
  .card svg.card-bg { position: absolute; inset: 0; width: 100%; height: 100%; }

  .card--front { left: 143px; top: 304px; background: var(--card-white); }
  .card--red { left: 630px; top: 210px; }
  .card--plain { left: 365px; top: 511px; background: var(--card-white); }

  .brand { position: absolute; display: flex; align-items: center; gap: 8px; }
  .brand-dot { border-radius: 50%; background: var(--red); flex: none; }
  .brand-name {
    font-family: "Cinzel", "Times New Roman", serif; font-weight: 600;
    color: var(--ink); white-space: nowrap; letter-spacing: .5px;
  }
  .card--front .brand { left: 20px; top: 26px; }
  .card--front .brand-dot { width: 34px; height: 34px; }
  .card--front .brand-name { font-size: 25px; }

  .person { position: absolute; left: 0; width: 205px; top: 148px; text-align: center; color: var(--text-light); }
  .person-name { font-size: 13px; font-weight: 700; }
  .person-line { font-size: 7.5px; line-height: 10px; }
  .person-web { position: absolute; left: 0; width: 205px; top: 206px; text-align: center; color: var(--text-light); font-size: 7.5px; font-weight: 700; }

  .addresses { position: absolute; left: 218px; top: 146px; color: var(--text-light); font-size: 7.5px; line-height: 10px; }
  .addresses p + p { margin-top: 7px; }

  .mini-brand { position: absolute; left: 18px; }
  .mini-brand .brand-dot { width: 14px; height: 14px; }
  .mini-brand .brand-name { font-size: 10px; }
  .card--red .mini-brand { top: 165px; }
  .card--red .mini-brand .brand-name { color: var(--text-light); }
  .card--red .mini-brand .brand-dot { background: var(--text-light); }
  .card--plain .mini-brand { top: 155px; }
  .mini-web { position: absolute; left: 18px; font-size: 7px; }
  .card--red .mini-web { top: 190px; color: var(--text-light); }
  .card--plain .mini-web { top: 183px; color: var(--ink); }

  .faint-decoration { position: absolute; border-radius: 50%; }
  .card--red .faint-decoration { right: 20px; top: 10px; width: 200px; height: 200px;
    background: radial-gradient(circle, rgba(255,120,120,.28), rgba(255,80,80,0) 70%); }
  .card--plain .faint-decoration { right: 25px; top: 12px; width: 210px; height: 210px;
    background: radial-gradient(circle, rgba(230,60,60,.22), rgba(230,60,60,0) 70%); }
</style>
</head>
<body>
<main class="canvas">

  <section class="card card--front" aria-label="Business card front">
    <svg class="card-bg" viewBox="0 0 420 234" preserveAspectRatio="none" aria-hidden="true">
      <defs>
        <linearGradient id="lowerLeft" x1="0" x2="1" y1="0" y2="0">
          <stop offset="0" stop-color="#2a0304"/>
          <stop offset="1" stop-color="#6d0a0d"/>
        </linearGradient>
        <linearGradient id="lowerRight" x1="0" x2="1" y1="0" y2="0">
          <stop offset="0" stop-color="#b10c14"/>
          <stop offset="1" stop-color="#e0141d"/>
        </linearGradient>
        <linearGradient id="whiteTop" x1="0" x2="0" y1="0" y2="1">
          <stop offset="0" stop-color="#ffffff"/>
          <stop offset="1" stop-color="#e6e6e6"/>
        </linearGradient>
      </defs>
      <rect width="420" height="234" fill="url(#whiteTop)"/>
      <path d="M0 118 C120 92 260 96 420 126 L420 234 L0 234 Z" fill="var(--wave-gray)"/>
      <path d="M0 124 C120 100 260 104 420 132 L420 234 L0 234 Z" fill="#1d1d1d"/>
      <path d="M0 132 C120 112 260 116 420 140 L420 234 L0 234 Z" fill="url(#lowerRight)"/>
      <path d="M0 132 C80 118 150 114 208 116 L208 234 L0 234 Z" fill="url(#lowerLeft)"/>
    </svg>
    <div class="brand">
      <span class="brand-dot"></span>
      <span class="brand-name">Torvel &amp; Company</span>
    </div>
    <div class="person">
      <p class="person-name">Marla Drosset</p>
      <p class="person-line">Founder, Torvel &amp; Company</p>
      <p class="person-line">Cell: 612.555.0142</p>
    </div>
    <p class="person-web">www.TorvelAndCo.example</p>
    <div class="addresses">
      <p>217 Meadow Lantern Dr.<br>Fernwood, Ohio 27584</p>
      <p>2816 Halloway Brook, NE<br>Ashford, Kansas 30361<br>Email: Marla@TorvelAndCo.example</p>
    </div>
  </section>

  <section class="card card--red" aria-label="Business card back, red">
    <svg class="card-bg" viewBox="0 0 420 234" preserveAspectRatio="none" aria-hidden="true">
      <defs>
        <radialGradient id="redGlow" cx=".6" cy=".4" r=".8">
          <stop offset="0" stop-color="#e8141e"/>
          <stop offset=".6" stop-color="#b50b12"/>
          <stop offset="1" stop-color="#6e0508"/>
        </radialGradient>
      </defs>
      <rect width="420" height="234" fill="url(#redGlow)"/>
    </svg>
    <div class="faint-decoration" role="img" aria-label="Large faint brand mark decoration"></div>
    <div class="brand mini-brand">
      <span class="brand-dot"></span>
      <span class="brand-name">Torvel &amp; Company</span>
    </div>
    <p class="mini-web">www.TorvelAndCo.example</p>
  </section>

  <section class="card card--plain" aria-label="Business card back, white">
    <div class="faint-decoration" role="img" aria-label="Large faint brand mark decoration"></div>
    <div class="brand mini-brand">
      <span class="brand-dot"></span>
      <span class="brand-name">Torvel &amp; Company</span>
    </div>
    <p class="mini-web">www.TorvelAndCo.example</p>
  </section>

</main>
</body>
</html>
```